Drinking and Driving course for the courts

Sophisitcated tri-fold brochure seen by judges, lawyers etc. People taking this course have been charged with drinking and driving (alcohol). Should be classy and upmarket. Please be creative like original brochure. Please use exact wording and in same order as brochure. Also please keep in approximately same place on brochure. Spelling and grammar should be exactly same as this document is already proof-read and checked by experts.

Target Market(s)

Judges, lawyers, court system.

Industry/Entity Type

Legal

Font styles to use
Serif

Requirements
Must have
• Creative and classy. Can look similar or same as original brochure. Should have pciture/graphic of car keys and drink
Nice to have
• A background graphic like in original brochure comes across very well. Subtle etc.
Should not have
• Does not need to have pictures of vehicles/cars. Definitely no brand names of cars or alcohol labels (or any kind).

```html
<!DOCTYPE html>
<html lang="en">
<head>
<meta charset="utf-8">
<title>Clear Minded – Tri-fold Brochure</title>
<link rel="stylesheet" href="https://fonts.googleapis.com/css2?family=Montserrat:ital,wght@0,300;0,400;0,500;0,600;0,700;0,800;1,300;1,400;1,700;1,800&display=swap">
<style>
:root{
  --bg:#e3e3e3;
  --slate:#5e5e5e;
  --gold:#ebc036;
  --gold-soft:#f0d064;
  --ink:#3b3b3b;
  --night:#1b191b;
  --black:#0d0d0d;
  --white:#ffffff;
  --navy:#1e2f6e;
}
*{box-sizing:border-box;margin:0;padding:0}
html,body{width:990px;height:1200px;overflow:hidden;background:var(--bg)}
body{font-family:"Montserrat",Arial,sans-serif;position:relative}
.sheet{position:absolute;left:156px;width:678px;height:523px;display:flex}
.sheet--outside{top:58px}
.sheet--inside{top:612px}
.panel{position:relative;width:226px;height:100%;overflow:hidden}
.abs{position:absolute}
.slate{background:var(--slate)}
.gold{background:var(--gold)}
.night{background:var(--night)}
.black{background:var(--black)}

/* background panel */
.bg-title{left:33px;top:72px;font-size:16.5px;font-weight:300;color:var(--gold);letter-spacing:.3px}
.bg-title b{font-weight:800}
.bg-copy{left:27px;width:186px;color:var(--gold-soft);font-size:6.6px;line-height:9.5px;text-align:justify;text-align-last:center;font-weight:400}
.bg-copy--lead{font-weight:700;color:var(--gold);text-align-last:left}
.bg-copy b{font-weight:700}
.bg-rule{left:80px;top:462px;width:73px;height:1px;background:var(--gold)}

/* cover middle */
.mission{left:0;width:226px;top:92px;text-align:center;font-style:italic;font-size:21px;line-height:25.7px;color:var(--ink);letter-spacing:.3px}
.mission .light{font-weight:300}
.mission .bold{font-weight:800}
.info-box{left:19px;top:412px;width:188px;height:75px;border:1px solid var(--ink);text-align:center}
.info-tab{left:33px;top:403px;width:160px;height:17px;background:var(--ink);color:var(--gold);font-size:8.5px;font-weight:600;text-align:center;line-height:17px}
.info-web{top:23px;width:100%;font-size:9.5px;font-weight:700;color:var(--ink)}
.info-line{width:100%;font-size:7.5px;color:var(--ink)}

/* cover front */
.cover-note{left:24px;top:66px;width:176px;height:74px;border:1px solid var(--gold);color:var(--gold);font-size:7.3px;font-weight:700;text-align:center;line-height:15px;padding-top:21px;letter-spacing:.2px}
.cover-course{left:0;width:226px;top:172px;text-align:center;color:var(--gold);font-size:8.3px;line-height:13.5px;letter-spacing:.3px}
.cover-course b{font-weight:700}
.white-base{left:0;top:330px;width:226px;height:193px;background:var(--white)}
.photo--keys{left:0;top:232px;width:226px;height:170px;background:linear-gradient(180deg,#1b191b 0%,#3a2a10 35%,#c9892a 55%,#f6f0e6 85%,#ffffff 100%)}
.brand{width:226px;text-align:center;color:var(--navy)}
.brand-name{font-size:13px;font-weight:800;letter-spacing:-.2px}
.brand-tag{font-size:6.5px;font-weight:600}
.brand-needs{font-size:6.3px;font-weight:600;line-height:9.5px}

/* inside left */
.ia-title{left:34px;top:54px;font-size:18.5px;font-weight:300;color:var(--ink);letter-spacing:.6px}
.ia-title b{font-weight:700}
.ia-box{left:25px;top:83px;width:187px;height:95px;border:1.5px solid var(--ink);padding:7px 8px;color:var(--ink);font-size:7px;font-weight:700;line-height:10.4px}
.ia-box p+p{margin-top:10px}
.bar{height:12px;background:var(--ink);color:var(--gold);font-size:7.3px;font-weight:700;line-height:12px;padding-left:8px;letter-spacing:.2px}
.bar--gold{background:var(--gold);color:var(--night);line-height:10.5px;height:auto;padding:1px 5px}
.list{color:var(--ink);font-size:6.8px;line-height:9.3px}
.list li{list-style:none;position:relative;padding-left:13px;margin-top:8px}
.list li span{position:absolute;left:0;font-weight:700}
.costs{left:34px;width:180px;color:var(--ink);font-size:6.8px;line-height:9.2px;display:grid;grid-template-columns:65px 1fr}
.costs dt{font-weight:700}

/* inside middle */
.lead-night{left:18px;top:54px;width:195px;color:var(--gold);font-size:7.3px;font-weight:700;line-height:10px}
.list--night{color:var(--gold-soft)}
.list--night li{padding-left:14px}
.list--night li span{font-weight:400}
.one-on-one{left:0;width:226px;top:296px;text-align:center;color:var(--gold);font-size:13.5px;font-weight:800;font-style:italic;line-height:17.5px;letter-spacing:.4px}
.photo--hand{left:0;top:330px;width:226px;height:193px;background:radial-gradient(ellipse at 55% 45%,#6b3a10 0%,#2a170a 35%,#0d0d0d 70%)}

/* inside right */
.remote{left:0;width:226px;top:40px;text-align:center;font-size:20px;font-weight:700;line-height:25px;letter-spacing:.5px}
.remote .w{color:var(--white)}
.remote .y{color:var(--gold)}
.icon-spot{left:61px;top:101px;width:102px;height:100px;background:linear-gradient(135deg,#f4f4f4,#d9d9d9);border-radius:6px}
.lower-gold{left:0;top:232px;width:226px;height:291px;background:var(--gold)}
.cost{left:0;width:226px;text-align:center;color:var(--ink)}
.cost-label{top:258px;font-size:15px;font-weight:300}
.cost-price{top:279px;font-size:16px;font-weight:700}
.product{top:322px;font-size:24.5px;font-weight:700;line-height:29px;letter-spacing:.5px}
</style>
</head>
<body>

<section class="sheet sheet--outside">
  <div class="panel slate">
    <h2 class="abs bg-title">OUR <b>BACKGROUND</b></h2>
    <p class="abs bg-copy bg-copy--lead" style="top:108px">Since its inception in 1998, Safe Lanes Driving School has strived to help drivers maintain their driving independence while leading safe and productive lives. Our motto “driving well for good” drives our vision of helping drivers across industries and at all stages of our driving careers.</p>
    <p class="abs bg-copy" style="top:178px">Safe Lanes started out working with school boards to deliver driver training to beginner drivers. Thousands of students have graduated from our ministry-approved curriculum throughout central Ontario. We are also ministry-approved to instruct defensive driving (DDC) and driver improvement courses (DIC), for drivers with speeding tickets, demerit points and at fault crashes.</p>
    <p class="abs bg-copy" style="top:273px">Safe Lanes has also evolved to provide comprehensive driver rehabilitation to those who have lost, or are at risk of losing their license for medical reasons. This includes mobility issues requiring adaptive equipment, as well as traumatic crashes resulting in cognitive impairments and PTSD. We work with clients before the courts charged with impaired driving (alcohol, cannabis, opioids), road rage and stunt driving.</p>
    <p class="abs bg-copy" style="top:376px">Founder <b>Daniel Hartley</b> started driving at an early age on his parent’s farm. Driving professionally and doing so safely is in his DNA. Daniel graduated from Northbrook College School, and obtained a degree in Business and Psychology from Carlton Ridge University. He is a certified in-car and in-class driving instructor and trainer.</p>
    <div class="abs bg-rule"></div>
  </div>

  <div class="panel gold">
    <h1 class="abs mission">
      <span class="light">MAINTAINING<br>DRIVING<br>INDEPENDENCE,</span><br>
      <span class="bold">WHILE LEADING<br>SAFE AND<br>PRODUCTIVE<br>LIVES!</span>
    </h1>
    <div class="abs info-box">
      <p class="abs info-web">www.safelanesdrivingschool.ca</p>
      <p class="abs info-line" style="top:42px"><b>Call</b>:705-555-0142</p>
      <p class="abs info-line" style="top:55px">dhartley@safelanesdrivingschool.ca</p>
    </div>
    <div class="abs info-tab">For more information:</div>
  </div>

  <div class="panel night">
    <div class="abs white-base"></div>
    <p class="abs cover-note">REFER ‘COVER PAGE’ ATTACHMENT<br>FOR COVER OPTIONS</p>
    <p class="abs cover-course"><b>A 1-DAY EDUCATIONAL COURSE</b><br>FOR THOSE CHARGED WITH<br>DRINKING AND DRIVING</p>
    <div class="abs photo--keys" role="img" aria-label="Photograph of a glass of whisky on ice beside a set of car keys"></div>
    <div class="abs brand" style="top:404px">
      <p class="brand-name">Safe Lanes Driving School</p>
      <p class="brand-tag" style="margin-top:3px">Driving well...for good!</p>
      <p class="brand-needs" style="margin-top:43px">For all your G License needs!<br>Beginner, Rehabilitation &amp; Remedial</p>
    </div>
  </div>
</section>

<section class="sheet sheet--inside">
  <div class="panel gold">
    <h2 class="abs ia-title">CLEAR <b>MINDED</b></h2>
    <div class="abs ia-box">
      <p>A 1-day, 7-hour, intensive remedial measures course for those charged with being under the influence of alcohol.</p>
      <p>Our goal is to equip our customers with knowledge and help them to avoid something devastating and/or irreversible from happening in the future.</p>
    </div>
    <div class="abs bar" style="left:27px;top:194px;width:186px">DURING THE COURSE WE WILL:</div>
    <div class="abs list" style="left:34px;top:208px;width:180px">
      <p>Look at how alcohol affects us from a physical standpoint:</p>
      <ul style="margin-left:10px">
        <li style="margin-top:5px"><span>I.</span>What is a serving of alcohol?</li>
        <li><span>II.</span>Blood alcohol concentration (BAC) and the many factors that go into creating our individual BAC/level of intoxication; how much does it take to get us to 0.05/0.08; how long to wear off?</li>
        <li><span>III.</span>Effects on different organs in the body including diabetes, cirrhosis etc.; effects on the brain/cognition at different levels of impairment</li>
      </ul>
    </div>
    <div class="abs bar" style="left:27px;top:362px;width:186px">COUNT THE COSTS INCLUDING:</div>
    <dl class="abs costs" style="top:380px">
      <dt>Financial:</dt><dd>fines, programs fees,<br>court costs, legal fees,<br>insurance</dd>
      <dt style="margin-top:26px">Human impact:</dt><dd style="margin-top:26px">personal relationships,<br>criminal record,<br>job prospects,<br>international travel,<br>custody, physical injury</dd>
    </dl>
  </div>

  <div class="panel black">
    <div class="abs photo--hand" role="img" aria-label="Photograph of a hand holding a glass of whisky in low light"></div>
    <p class="abs lead-night">Help you gain a thorough understanding of the laws in Ontario &amp; Canada (the Highway Traffic Act &amp; Criminal Code of Canada)</p>
    <div class="abs bar bar--gold" style="left:14px;top:92px;width:197px">LOOK AT THE PSYCHOLOGY OF ADDICTION:</div>
    <ul class="abs list list--night" style="left:24px;top:107px;width:184px">
      <li style="margin-top:0"><span>I.</span>Stages of change model (how to improve our habits)</li>
      <li><span>II.</span>Define and explore neuroplasticity and the established science behind how we train and can retrain the brain</li>
    </ul>
    <div class="abs bar bar--gold" style="left:14px;top:173px;width:197px">REFLECTIVE STUDY BASED ON WHAT THE NIGHT OUT LOOKS LIKE:</div>
    <ul class="abs list list--night" style="left:24px;top:203px;width:184px">
      <li style="margin-top:0"><span>I.</span>Triggers and events leading up to the arrest</li>
      <li><span>II.</span>Alternatives--what tangible things can we do differently moving forward?</li>
    </ul>
    <p class="abs list list--night" style="left:18px;top:251px;width:190px">Look at how genetics and role models influence our learned behaviours</p>
    <p class="abs one-on-one">COURSES ARE<br>ONE-ON-ONE.</p>
  </div>

  <div class="panel slate">
    <div class="abs lower-gold"></div>
    <h2 class="abs remote"><span class="w">OFFERED</span><br><span class="y">REMOTELY!</span></h2>
    <div class="abs icon-spot" role="img" aria-label="Icon of a computer screen showing a person with a speech bubble"></div>
    <p class="abs cost cost-label">Course Cost:</p>
    <p class="abs cost cost-price">$775.00 + HST.</p>
    <p class="abs cost product">CLEAR<br>MINDED</p>
    <div class="abs brand" style="top:408px">
      <p class="brand-name">Safe Lanes Driving School</p>
      <p class="brand-tag" style="margin-top:3px">Driving well...for good!</p>
      <p class="brand-needs" style="margin-top:40px">For all your G License needs!<br>Beginner, Rehabilitation &amp; Remedial</p>
    </div>
  </div>
</section>

</body>
</html>
```